Postcard Design

our company name is wexford lane haven.we provide face to face psychic tarot reading and crystal healing in a very exclusive and private clinic. we provide answers and guidance for future life event and the balance for the body and soul.we are base in 17 wexford lane in london .we want a card who say what we do as clear as possible and who is eye catching to people so when they see it want to read it this is our web site www.wexfordlnhaven.co.uk you need to put number on it to call us the number ContacUs:
0208 594 3216
0788 213 5072

Industry/Entity Type

Clinic

```html
<!DOCTYPE html>
<html lang="en">
<head>
<meta charset="utf-8">
<title>Wexford Lane Haven – Postcard</title>
<link rel="stylesheet" href="https://fonts.googleapis.com/css2?family=Noto+Sans&family=Gochi+Hand&family=Didact+Gothic&family=Oswald:wght@700&display=swap">
<style>
  :root {
    --card-yellow: #f7ec4a;
    --ink: #111111;
    --ink-navy: #1b1b2f;
    --accent-red: #e3312a;
    --photo-white: #ffffff;
    --frame-black: #000000;
  }
  html, body {
    margin: 0;
    padding: 0;
    width: 1200px;
    height: 1000px;
    overflow: hidden;
    background: #ffffff;
  }
  .postcard {
    position: relative;
    width: 1200px;
    height: 1000px;
    font-family: "Noto Sans", sans-serif;
    color: var(--ink);
  }
  .postcard__border {
    position: absolute;
    left: 0;
    top: 0;
  }
  .photo {
    position: absolute;
    box-sizing: border-box;
  }
  .photo--healing {
    left: 73px; top: 95px; width: 239px; height: 177px;
    background: var(--photo-white);
    padding: 13px 12px 10px 12px;
  }
  .photo--tarot {
    left: 320px; top: 95px; width: 241px; height: 177px;
    background: var(--frame-black);
    padding: 10px 10px 10px 10px;
  }
  .photo__fill {
    width: 100%;
    height: 100%;
  }
  .photo--healing .photo__fill {
    background: linear-gradient(135deg, #6f625a 0%, #9a8f86 45%, #5b5048 100%);
  }
  .photo--tarot .photo__fill {
    background: linear-gradient(100deg, #e6d49a 0%, #c9a45a 40%, #8a8e86 70%, #e8e2cf 100%);
  }
  .intro {
    position: absolute;
    left: 85px; top: 284px;
    margin: 0;
    font-size: 21px;
    line-height: 27px;
    width: 480px;
  }
  .services {
    position: absolute;
    left: 60px; top: 380px;
    width: 510px;
    text-align: center;
    margin: 0;
  }
  .services__item {
    display: block;
    font-family: "Gochi Hand", cursive;
    color: var(--accent-red);
    font-size: 38px;
    line-height: 44px;
    letter-spacing: 3px;
    text-transform: uppercase;
  }
  .services__join {
    display: block;
    font-size: 20px;
    line-height: 24px;
    margin: 2px 0 4px;
  }
  .sender {
    position: absolute;
    left: 85px; top: 585px;
    font-family: "Didact Gothic", sans-serif;
  }
  .sender__label {
    font-size: 31px;
    margin: 0 0 26px;
    line-height: 36px;
  }
  .sender__name {
    font-family: "Oswald", sans-serif;
    font-weight: 700;
    font-size: 29px;
    line-height: 34px;
    color: var(--ink-navy);
    text-transform: uppercase;
    margin: 0;
  }
  .sender__address {
    font-style: normal;
    font-size: 29px;
    line-height: 37px;
    margin: 0 0 24px;
  }
  .sender__contact {
    font-size: 22px;
    line-height: 30px;
    margin: 0;
  }
  .divider {
    position: absolute;
    left: 599px; top: 242px;
    width: 3px; height: 580px;
    background: var(--ink);
  }
  .stamp {
    position: absolute;
    left: 876px; top: 116px;
    width: 236px; height: 246px;
    background: linear-gradient(135deg, #ffffff 0%, #ededed 60%, #d8d8d8 100%);
  }
  .recipient {
    position: absolute;
    left: 650px; top: 418px;
    width: 412px;
  }
  .recipient__label {
    font-family: "Didact Gothic", sans-serif;
    font-size: 36px;
    line-height: 40px;
    margin: 0;
  }
  .recipient__line {
    position: absolute;
    left: 0;
    width: 412px;
    height: 3px;
    background: var(--ink);
  }
</style>
</head>
<body>
<main class="postcard">
  <svg class="postcard__border" width="1200" height="1000" viewBox="0 0 1200 1000" aria-hidden="true">
    <rect x="0" y="55" width="1182" height="885" fill="var(--card-yellow)"/>
    <rect x="3" y="56" width="1178" height="884" fill="none" stroke="var(--ink)" stroke-width="3"
          stroke-dasharray="22 8 6 8 6 8 6 8"/>
  </svg>

  <figure class="photo photo--healing" style="margin:0">
    <div class="photo__fill" role="img" aria-label="Photo of a woman lying down with healing crystals placed on her face"></div>
  </figure>
  <figure class="photo photo--tarot" style="margin:0">
    <div class="photo__fill" role="img" aria-label="Photo of three illustrated tarot cards fanned out"></div>
  </figure>

  <p class="intro">Health is wealth. We always ensure that our customers always living healthy life. Welcome to our clinic for</p>

  <p class="services">
    <span class="services__item">Psychic Tarot Reading</span>
    <span class="services__join">and</span>
    <span class="services__item">Crystal Healing</span>
  </p>

  <section class="sender">
    <p class="sender__label">From,</p>
    <h1 class="sender__name">Wexford Lane Haven</h1>
    <address class="sender__address">17 Wexford Lane<br>London</address>
    <p class="sender__contact">www.wexfordlnhaven.co.uk<br>0208 594 3216<br>0788 213 5072</p>
  </section>

  <div class="divider"></div>

  <div class="stamp" role="img" aria-label="Stamp area with a decorative diamond border"></div>

  <section class="recipient">
    <p class="recipient__label">To,</p>
    <span class="recipient__line" style="top:40px"></span>
    <span class="recipient__line" style="top:90px"></span>
    <span class="recipient__line" style="top:143px"></span>
    <span class="recipient__line" style="top:192px"></span>
  </section>
</main>
</body>
</html>
```